E-Liquid Bottle Labels

We are looking to redesign the label on our e-cigarette juice bottles.

We are trying to brand our company "Copper Lantern Mists" by using the Copper Lantern portion of our logo prominently on our current labels. The goal is to have customers know our product when they just see the diamond and not need to read our name to know its a Copper Lantern Premium E-Liquid.

We carry 50 different flavors that each come in 5 sizes. Additionally each size comes in 4 different levels of nicotine strength (0 mg, 6 mg, 12 mg, and 18 mg) Due to label cost runs we need to put each nicotine strengths on the label with a "checkbox" system next to them so we can manually mark the correct mg strength on each bottle after applying the label.

The labels should include the following:

1- The Copper Lantern in our logo as the focal point
2- The name "Copper Lantern Mists" in our logo font Trajan Bold Pro
3- The words "Premium E-Liquid"
4- The name of the Premium E-Liquid. We have 50 flavors (please see attached flavor grid with the shortest name being "Kiwi" and the longest being "Banana Cream Menthol")
5- The following text "Caution: This product contains Nicotine. Keep out of the reach of children and pets. Do not drink. Not for sale to minors.
6- The following text "Ingredients: Propylene Glycol (USP),Glycerin (USP), L-Nicotine, FEMA/GRAS approved Natural and Artificial Flavorings. All ingredients are FDA approved for human consumption.
7- Some type of checkbox set up to mark whether the juice has "0 mg", "6 mg", "12 mg", or "18 mg" of nicotine

Although the same design will be used across all bottle sizes. We will need to make sure that the design gets a finished version in all 5 sizes.

There are 5 sizes of labels:

1- 15 ml squeeze is 2 3/4" wide x 1 5/8" high
2- 30 ml squeeze is 3 1/2" wide x 1 3/4" high
3- 15 ml glass is 3" wide x 1 1/4" high
4- 30 ml glass is 3 5/8" wide x 1 1/2" high
5- 60 ml glass is 4 5/8" wide x 1 3/4" high

Colors
0455a3
3176b5
85acd3
ceddec
0692cd
33a6d7
85cae6
cee9f5

```html
<!DOCTYPE html>
<html lang="en">
<head>
<meta charset="utf-8">
<title>Copper Lantern Mists – Premium E-Liquid Label</title>
<link rel="stylesheet" href="https://fonts.googleapis.com/css2?family=Cinzel:wght@600;700&family=Carlito:wght@400;700&display=swap">
<style>
  :root {
    --brand-blue: #0455a3;
    --mid-blue: #3176b5;
    --soft-blue: #85acd3;
    --pale-blue: #ceddec;
    --sky-blue: #85cae6;
    --ice-blue: #cee9f5;
    --ink: #111111;
    --paper: #ffffff;
    --backdrop: #f4f4f4;
  }
  * { box-sizing: border-box; margin: 0; padding: 0; }
  html, body {
    width: 1200px; height: 1200px; overflow: hidden;
    background: var(--backdrop);
  }
  .canvas { position: relative; width: 1200px; height: 1200px; }

  .label {
    position: absolute; left: 18px; top: 380px;
    width: 1164px; height: 440px;
    background: var(--paper);
    border-radius: 14px;
    overflow: hidden;
    font-family: "Carlito", "Calibri", sans-serif;
    color: var(--ink);
  }

  .label-header {
    position: absolute; left: 0; top: 0; width: 100%; height: 88px;
    background: var(--brand-blue);
    display: flex; align-items: center; justify-content: center;
  }
  .brand-name {
    font-family: "Cinzel", serif; font-weight: 700;
    color: var(--paper); font-size: 40px; letter-spacing: 1px;
  }
  .brand-name .initial { font-size: 50px; }

  .ingredients {
    position: absolute; left: 49px; top: 130px;
    text-align: left; white-space: nowrap;
  }
  .panel-heading { font-weight: 700; font-size: 17px; margin-bottom: 13px; }
  .panel-text { font-size: 17.5px; line-height: 24.5px; }

  .caution {
    position: absolute; right: 48px; top: 130px;
    text-align: right; white-space: nowrap;
  }

  .strength {
    position: absolute; right: 48px; top: 280px;
    text-align: right;
  }
  .strength-title { font-weight: 700; font-size: 14px; margin-bottom: 6px; }
  .strength-options { display: flex; gap: 10px; justify-content: flex-end; }
  .strength-option { position: relative; width: 36px; height: 36px; }
  .strength-option svg { position: absolute; inset: 0; }
  .strength-option span {
    position: absolute; inset: 0;
    display: flex; align-items: center; justify-content: center;
    font-size: 17px;
  }

  .brand-mark {
    position: absolute; left: 432px; top: 126px; width: 300px; height: 200px;
    display: flex; flex-direction: column; align-items: center; justify-content: center; gap: 14px;
  }
  .brand-mark-dot {
    width: 70px; height: 70px; border-radius: 50%;
    background: var(--brand-blue);
  }
  .brand-mark-name {
    font-family: "Cinzel", serif; font-weight: 700;
    color: var(--brand-blue); font-size: 32px; letter-spacing: 1px;
    white-space: nowrap;
  }

  .flavor-box {
    position: absolute; left: 418px; top: 340px; width: 328px; height: 50px;
    border: 2px solid var(--ink); border-radius: 7px;
    display: flex; align-items: center; justify-content: center;
    font-size: 24px;
  }

  .label-footer {
    position: absolute; left: 0; bottom: 0; width: 100%; height: 36px;
    background: var(--brand-blue);
    display: flex; align-items: center; justify-content: center;
  }
  .tagline {
    font-family: "Cinzel", serif; font-weight: 600;
    color: var(--paper); font-size: 22px; letter-spacing: 5px;
  }
  .tagline .initial { font-size: 26px; }
</style>
</head>
<body>
<div class="canvas">
  <section class="label">
    <header class="label-header">
      <h1 class="brand-name"><span class="initial">C</span>OPPER <span class="initial">L</span>ANTERN <span class="initial">M</span>ISTS</h1>
    </header>

    <div class="ingredients">
      <h2 class="panel-heading">INGREDIENTS:</h2>
      <p class="panel-text">Propylene Glycol (USP),<br>Glycerin (USP), L-Nicotine,<br>FEMA/GRAS Approved<br>Natural / Artificial Flavoring.<br>All ingredients are FDA<br>approved for human con-<br>sumption.</p>
    </div>

    <div class="brand-mark">
      <div class="brand-mark-dot"></div>
      <div class="brand-mark-name">Copper Lantern</div>
    </div>

    <div class="flavor-box">Harbor Mint</div>

    <div class="caution">
      <h2 class="panel-heading">CAUTION :</h2>
      <p class="panel-text">This product contains nicotine.<br>Keep out of reach of children<br>and pets. Do not drink.<br>Not for sale to minors.</p>
    </div>

    <div class="strength">
      <p class="strength-title">Nicotines in miligram:</p>
      <div class="strength-options">
        <div class="strength-option">
          <svg viewBox="0 0 36 36"><circle cx="18" cy="18" r="16" fill="none" stroke="var(--sky-blue)" stroke-width="3"/></svg>
          <span>0</span>
        </div>
        <div class="strength-option">
          <svg viewBox="0 0 36 36"><circle cx="18" cy="18" r="16" fill="none" stroke="var(--sky-blue)" stroke-width="3"/><circle cx="18" cy="18" r="16" fill="none" stroke="var(--mid-blue)" stroke-width="3" stroke-dasharray="25 101" transform="rotate(-90 18 18)"/></svg>
          <span>6</span>
        </div>
        <div class="strength-option">
          <svg viewBox="0 0 36 36"><circle cx="18" cy="18" r="16" fill="none" stroke="var(--soft-blue)" stroke-width="3"/><circle cx="18" cy="18" r="16" fill="none" stroke="var(--brand-blue)" stroke-width="3" stroke-dasharray="60 101" transform="rotate(-90 18 18)"/></svg>
          <span>12</span>
        </div>
        <div class="strength-option">
          <svg viewBox="0 0 36 36"><circle cx="18" cy="18" r="16" fill="none" stroke="var(--brand-blue)" stroke-width="3"/></svg>
          <span>18</span>
        </div>
      </div>
    </div>

    <footer class="label-footer">
      <p class="tagline"><span class="initial">P</span>REMIUM <span class="initial">E</span>-<span class="initial">L</span>IQUID</p>
    </footer>
  </section>
</div>
</body>
</html>
```